North American Image Consultant needs a process design and a method design

I am an Image/style consultant who works with business professionals in the Toronto area. My product name is called " R.E.S.K.A." I help people understand how your " Position, Industry, Volume, effects their Outcome and Time. I help people create a professional appearance in a business casual/digital world, from head to toe. I work with them through all 4 seasons, to achieve consistency and confidence to help them look and feel amazing, inside and out.. easily and effortlessly. My main colour is aqua blue, I don't want any neon or primary colours. I would like it to appeal to both men and women ( but mostly women)
The final design should be an easy to follow path to success with an understanding of what R.E.S.K.A will do for them.

Target Market(s)

mid level executive business professionals 38-58 yrs old they want to look and feel amazing inside and out. They want to up their game, get the promotion, nail the interview , and feel they're relevant and taken seriously in a leadership way.

Font styles to use
Serif

Colors
b7a5cd
886aae
85cae6
33a6d7
33b8a4
f04a50
00a990
e34297
85acd3

Requirements
Must have
• A classy, casual feel. A positive feel good feeling
Nice to have
• A 3 colour balance ( Not black based)
Should not have
• Too many squares
too many squiggly lines.
Not too masculine/feminine
too childish/youthful
Not office focused or bank focused

```html
<!DOCTYPE html>
<html lang="en">
<head>
<meta charset="utf-8">
<title>R.E.S.K.A. — Maintaining a professional appearance in a business casual world</title>
<link rel="stylesheet" href="https://fonts.googleapis.com/css2?family=Merriweather:wght@400;900&display=swap">
<style>
  :root {
    --teal: #33b8a4;
    --sky: #85cae6;
    --blue: #33a6d7;
    --violet: #886aae;
    --lilac: #b7a5cd;
    --ink: #111111;
    --muted: #7d7d7d;
    --rule: #a6a6a6;
    --paper: #ffffff;
  }
  html, body {
    margin: 0;
    padding: 0;
    width: 1200px;
    height: 675px;
    overflow: hidden;
    background: var(--paper);
  }
  .canvas { display: block; width: 1200px; height: 675px; }
  .brand-title { font-family: "Merriweather", Georgia, serif; font-weight: 900; font-size: 48px; fill: var(--ink); }
  .tagline { font-family: "Merriweather", Georgia, serif; font-weight: 400; font-size: 42px; fill: var(--muted); }
  .header-rule { stroke: var(--rule); stroke-width: 7; }
  .step-title { font-family: "Merriweather", Georgia, serif; font-weight: 900; font-size: 46px; fill: var(--ink); }
  .step-text { font-family: "Merriweather", Georgia, serif; font-weight: 400; font-size: 32px; fill: var(--ink); }
  .petal-ring { fill: none; stroke: var(--paper); stroke-width: 5; }
  .path-seg { fill: none; stroke-width: 8; stroke-linecap: round; }
  .connector { stroke-width: 8; stroke-linecap: round; }
  .node-ring { fill: var(--paper); stroke-width: 7; }
  .icon { fill: none; stroke: currentColor; stroke-width: 4; stroke-linecap: round; stroke-linejoin: round; }
  .c-teal { color: var(--teal); }
  .c-sky { color: var(--sky); }
  .c-blue { color: var(--blue); }
  .c-violet { color: var(--violet); }
  .c-lilac { color: var(--lilac); }
  .c-white { color: var(--paper); }
</style>
</head>
<body>
<svg class="canvas" viewBox="0 0 2560 1440" xmlns="http://www.w3.org/2000/svg">
  <defs>
    <path id="petal-shape" d="M0,-28 L112.5,-153.5 A145 145 0 1 0 -112.5,-153.5 Z"/>

    <symbol id="icon-position" viewBox="0 0 100 100">
      <g class="icon">
        <circle cx="50" cy="14" r="9"/>
        <path d="M36 38 Q36 25 50 25 Q64 25 64 38 Z"/>
        <path d="M50 38 V50 M18 50 H82 M18 50 V60 M50 50 V60 M82 50 V60"/>
        <circle cx="18" cy="68" r="7"/>
        <circle cx="50" cy="68" r="7"/>
        <circle cx="82" cy="68" r="7"/>
        <path d="M7 92 Q7 77 18 77 Q29 77 29 92 Z"/>
        <path d="M39 92 Q39 77 50 77 Q61 77 61 92 Z"/>
        <path d="M71 92 Q71 77 82 77 Q93 77 93 92 Z"/>
      </g>
    </symbol>

    <symbol id="icon-industry" viewBox="0 0 100 100">
      <g class="icon">
        <circle cx="55" cy="27" r="16"/>
        <circle cx="55" cy="22" r="5"/>
        <path d="M46 37 Q46 29 55 29 Q64 29 64 37"/>
        <circle cx="24" cy="74" r="14"/>
        <circle cx="24" cy="70" r="4.5"/>
        <path d="M16 83 Q16 76 24 76 Q32 76 32 83"/>
        <circle cx="76" cy="74" r="14"/>
        <circle cx="76" cy="70" r="4.5"/>
        <path d="M68 83 Q68 76 76 76 Q84 76 84 83"/>
        <path d="M46 40 L30 61 M64 40 L71 61"/>
        <path d="M39 27 H20 L15 15 M71 20 H88 M71 32 H84 V42"/>
        <circle cx="14" cy="12" r="3"/>
        <circle cx="91" cy="20" r="3"/>
        <circle cx="84" cy="46" r="4"/>
        <path d="M36 84 L44 93 H50"/>
        <circle cx="53" cy="93" r="3"/>
      </g>
    </symbol>

    <symbol id="icon-volume" viewBox="0 0 100 100">
      <g class="icon">
        <path d="M22 62 L58 22 L80 70 Z"/>
        <path d="M58 22 Q66 14 74 28 L82 50 Q86 64 80 70"/>
        <path d="M22 62 L14 70 Q10 76 16 82 L22 86 Q28 90 34 84 L42 76"/>
        <path d="M36 70 L54 92 L62 86 L46 68"/>
        <path d="M72 10 Q80 14 82 22 M78 4 Q90 10 92 22"/>
      </g>
    </symbol>

    <symbol id="icon-outcome" viewBox="0 0 100 100">
      <g class="icon">
        <path d="M26 8 H74 V34 Q74 62 50 62 Q26 62 26 34 Z"/>
        <path d="M26 14 H8 V26 Q8 40 26 44 M74 14 H92 V26 Q92 40 74 44"/>
        <circle cx="50" cy="34" r="14"/>
        <path d="M50 25 L53 31 L59 32 L54.5 36 L56 42 L50 39 L44 42 L45.5 36 L41 32 L47 31 Z"/>
        <path d="M44 62 V80 M56 62 V80"/>
        <path d="M32 92 Q32 80 50 80 Q68 80 68 92 Z"/>
      </g>
    </symbol>

    <symbol id="icon-time" viewBox="0 0 100 100">
      <g class="icon">
        <circle cx="48" cy="56" r="38"/>
        <circle cx="48" cy="56" r="30"/>
        <path d="M40 18 V10 H56 V18 M36 6 H60"/>
        <path d="M76 24 L84 16 M80 12 L90 22"/>
        <path d="M48 30 V35 M48 77 V82 M22 56 H27 M69 56 H74"/>
        <path d="M48 56 L60 40"/>
        <circle cx="48" cy="56" r="4"/>
      </g>
    </symbol>
  </defs>

  <!-- Header -->
  <header>
    <text class="brand-title" x="205" y="157">R.E.S.K.A.</text>
    <text class="tagline" x="2380" y="157" text-anchor="end">Maintaining a professional appearance in a business casual world</text>
    <line class="header-rule" x1="205" y1="174" x2="2380" y2="174"/>
  </header>

  <!-- Flower of five steps -->
  <g class="flower" transform="translate(787 800)">
    <g transform="rotate(0)">
      <use href="#petal-shape" fill="var(--teal)"/>
      <circle class="petal-ring" cx="0" cy="-250" r="115"/>
    </g>
    <g transform="rotate(72)">
      <use href="#petal-shape" fill="var(--sky)"/>
      <circle class="petal-ring" cx="0" cy="-250" r="115"/>
    </g>
    <g transform="rotate(144)">
      <use href="#petal-shape" fill="var(--blue)"/>
      <circle class="petal-ring" cx="0" cy="-250" r="115"/>
    </g>
    <g transform="rotate(-144)">
      <use href="#petal-shape" fill="var(--violet)"/>
      <circle class="petal-ring" cx="0" cy="-250" r="115"/>
    </g>
    <g transform="rotate(-72)">
      <use href="#petal-shape" fill="var(--lilac)"/>
      <circle class="petal-ring" cx="0" cy="-250" r="115"/>
    </g>
  </g>
  <g class="flower-icons c-white">
    <use href="#icon-position" x="727" y="490" width="120" height="120"/>
    <use href="#icon-industry" x="968" y="663" width="120" height="120"/>
    <use href="#icon-volume" x="874" y="942" width="120" height="120"/>
    <use href="#icon-outcome" x="580" y="942" width="120" height="120"/>
    <use href="#icon-time" x="489" y="663" width="120" height="120"/>
  </g>

  <!-- Path arc -->
  <g class="journey">
    <path class="path-seg" stroke="var(--teal)" d="M1140 413 A380 377 0 0 1 1368 490"/>
    <path class="path-seg" stroke="var(--sky)" d="M1368 490 A380 377 0 0 1 1502 676"/>
    <path class="path-seg" stroke="var(--blue)" d="M1502 676 A380 377 0 0 1 1498 913"/>
    <path class="path-seg" stroke="var(--violet)" d="M1498 913 A380 377 0 0 1 1365 1097"/>
    <path class="path-seg" stroke="var(--lilac)" d="M1365 1097 A380 377 0 0 1 1140 1170"/>

    <line class="connector" stroke="var(--teal)" x1="1265" y1="433" x2="1497" y2="433"/>
    <line class="connector" stroke="var(--sky)" x1="1460" y1="576" x2="1684" y2="576"/>
    <line class="connector" stroke="var(--blue)" x1="1520" y1="791" x2="1755" y2="791"/>
    <line class="connector" stroke="var(--violet)" x1="1458" y1="1004" x2="1687" y2="1004"/>
    <line class="connector" stroke="var(--lilac)" x1="1262" y1="1150" x2="1494" y2="1150"/>

    <circle cx="1140" cy="413" r="12" fill="var(--teal)"/>
    <circle cx="1140" cy="1170" r="12" fill="var(--lilac)"/>
    <circle class="node-ring" cx="1368" cy="490" r="12" stroke="var(--teal)"/>
    <circle class="node-ring" cx="1502" cy="676" r="12" stroke="var(--sky)"/>
    <circle class="node-ring" cx="1498" cy="913" r="12" stroke="var(--blue)"/>
    <circle class="node-ring" cx="1365" cy="1097" r="12" stroke="var(--violet)"/>
  </g>

  <!-- Step legend -->
  <g class="legend">
    <g class="step step-position">
      <use class="c-teal" href="#icon-position" x="1702" y="350" width="88" height="88"/>
      <text class="step-title" x="1818" y="382">P - Position</text>
      <text class="step-text" x="1818" y="430">Level of authority</text>
    </g>
    <g class="step step-industry">
      <use class="c-sky" href="#icon-industry" x="1848" y="551" width="88" height="88"/>
      <text class="step-title" x="1973" y="584">I - Industry</text>
      <text class="step-text" x="1973" y="633">Influence of environment</text>
    </g>
    <g class="step step-volume">
      <use class="c-blue" href="#icon-volume" x="1960" y="736" width="80" height="80"/>
      <text class="step-title" x="2086" y="764">V - Volume</text>
      <text class="step-text" x="2086" y="812">The ‘Sound’ of your presence</text>
      <text class="step-text" x="2086" y="851">when you walk into a room</text>
    </g>
    <g class="step step-outcome">
      <use class="c-violet" href="#icon-outcome" x="1859" y="953" width="82" height="82"/>
      <text class="step-title" x="1984" y="988">O - Outcome</text>
      <text class="step-text" x="1984" y="1037">Achieve consistent results</text>
    </g>
    <g class="step step-time">
      <use class="c-lilac" href="#icon-time" x="1704" y="1148" width="82" height="82"/>
      <text class="step-title" x="1825" y="1178">T - Time</text>
      <text class="step-text" x="1825" y="1226">Save more, spend less</text>
    </g>
  </g>
</svg>
</body>
</html>
```